web page design with coding

We are a start up insurance agency who needs to design a full functional web page. we recently did a postcard design though brightloom I will upload the final project for you to see the color scheme/font we would like to continue to use. I also have a rough draft of verbage I would like our website to have. I will upload that as well.

Reason: I am sorry but the person who will make the final decision on the website is out of the country at the moment and will make the final decision when he returns.

Insurance

```html
<!DOCTYPE html>
<html lang="en">
<head>
<meta charset="utf-8">
<title>Crestmark Insurance Group</title>
<link href="https://fonts.googleapis.com/css2?family=Open+Sans:wght@300;400;600;700&display=swap" rel="stylesheet">
<style>
:root{
  --navy:#1b2f66;
  --navy-deep:#142451;
  --slate:#2a2f3e;
  --gold:#a8792f;
  --brown:rgba(128,92,48,.88);
  --red:#e8191c;
  --bar:#262a36;
  --light:#e4e4e4;
  --ink:#555;
  --white:#fff;
}
*{margin:0;padding:0;box-sizing:border-box}
html,body{width:1200px;height:3010px;overflow:hidden}
body{font-family:"Open Sans",Arial,sans-serif;background:#fff;position:relative;color:var(--ink)}
.abs{position:absolute}
ul{list-style:none}

/* top navigation */
.topnav{left:0;top:0;width:1200px;height:36px;background:#2c2c2c;display:flex;align-items:center}
.topnav ul{display:flex;margin-left:70px;height:36px}
.topnav li{font-size:14px;font-weight:600;color:#fff;padding:0 18px;line-height:36px;border-right:1px solid #555}
.topnav li.active{background:var(--gold)}
.topnav .login{position:absolute;right:76px;font-size:14px;font-weight:600;color:#fff}

/* brand band */
.brandbar{left:0;top:36px;width:1200px;height:88px;background:var(--light);display:flex;justify-content:center;align-items:center}
.brand{display:flex;align-items:center;gap:10px;font-size:18px;font-weight:600;color:#333;letter-spacing:.3px}
.brand .mark{width:12px;height:12px;background:#333}

/* hero */
.hero{left:0;top:124px;width:1200px;height:554px;background:linear-gradient(180deg,#3d3a5c 0%,#8a6a78 30%,#c9906e 48%,#4c4a62 62%,#2c2b3c 100%)}
.hero-text{left:70px;top:384px;color:#fff;width:530px}
.hero-text .l1{font-size:42px;font-weight:300;line-height:48px}
.hero-text .l2{font-size:50px;font-weight:700;line-height:58px}
.hero-text .l3{font-size:42px;font-weight:300;line-height:44px;text-align:right}

.quote{left:756px;top:198px;width:380px;height:480px;background:var(--brown)}
.quote h2{height:74px;background:var(--gold);color:#fff;font-size:25px;font-weight:600;line-height:74px;padding-left:38px}
.field{position:absolute;left:34px;width:310px;height:38px;background:#fff;border-radius:3px;font-size:15px;color:#666;line-height:38px;padding-left:16px}
.typebox{position:absolute;left:34px;top:250px;width:310px;height:118px;background:#fff;border-radius:3px;padding:10px 16px;font-size:15px;color:#555}
.typebox .opts{display:grid;grid-template-columns:1fr 1fr;row-gap:6px;margin-top:10px;padding-left:12px}
.typebox .opts span{display:flex;align-items:center;gap:8px}
.typebox i{width:11px;height:11px;border:1.5px solid #666;border-radius:50%;display:inline-block}
.typebox i.on{background:radial-gradient(#444 40%,#fff 45%)}
.quote-btn{position:absolute;left:34px;top:376px;width:310px;height:52px;background:var(--navy);color:#fff;font-size:19px;font-weight:700;display:flex;justify-content:center;align-items:center;gap:18px;border-radius:2px}
.quote-note{position:absolute;left:30px;top:436px;width:320px;font-size:11px;color:#fff;text-align:center;line-height:14px}

/* about */
.about{left:0;top:678px;width:1200px;height:372px;background:linear-gradient(90deg,#f4f5f7,#e6e8ee 40%,#dfe3ea 70%,#f3f4f6)}
.about-photo{left:0;top:0;width:1200px;height:372px;opacity:.35;background:radial-gradient(ellipse 120px 180px at 330px 200px,#b8bfcc,transparent),radial-gradient(ellipse 120px 180px at 830px 190px,#b8bfcc,transparent),radial-gradient(ellipse 110px 170px at 590px 210px,#c5cbd6,transparent)}
.about h2{position:absolute;top:42px;width:1200px;text-align:center;font-size:24px;font-weight:400;color:var(--navy)}
.about .sub{position:absolute;top:88px;width:1200px;text-align:center;font-size:15px;color:#777;letter-spacing:.5px}
.about .rule{position:absolute;left:576px;top:122px;width:48px;height:6px;background:var(--navy)}
.about p{position:absolute;left:160px;top:160px;width:880px;text-align:center;font-size:13.5px;color:#888;line-height:28px}
.btn-red{background:var(--red);color:#fff;font-size:14px;font-weight:600;display:flex;justify-content:center;align-items:center}
.about .btn-red{position:absolute;left:518px;top:280px;width:158px;height:46px}

/* insurance panels */
.panel{top:1050px;height:818px}
.panel.personal{left:0;width:598px;background:linear-gradient(160deg,#1d3471,#182b5e)}
.panel.business{left:600px;width:600px;background:linear-gradient(160deg,#2d3242,#23283a)}
.panel h3{position:absolute;left:72px;top:70px;font-size:20px;font-weight:400;color:#fff;width:490px;padding-bottom:18px;border-bottom:2px solid #fff}
.panel.business h3{left:44px;width:490px}
.items{position:absolute;top:162px;display:grid;grid-template-columns:264px 260px;grid-auto-rows:104px}
.personal .items{left:72px}
.business .items{left:44px;grid-template-columns:268px 280px}
.item{display:flex;align-items:center;gap:16px;color:#fff;font-size:15px;line-height:18px;height:104px}
.item svg{flex:none;width:56px;height:56px}
.panel .btn-red{position:absolute;top:706px;width:158px;height:46px}
.personal .btn-red{left:230px}
.business .btn-red{left:206px}

.tip{left:724px;top:1384px;width:314px;height:158px;background:#fff;border-radius:3px;padding:18px 20px;font-size:13px;color:#333;line-height:18px;box-shadow:0 2px 6px rgba(0,0,0,.3)}
.tip .more{position:absolute;right:20px;bottom:10px;color:var(--red);font-size:13px}

/* partners */
.partners{left:0;top:1868px;width:1200px;height:144px;background:var(--light)}
.badge{position:absolute;top:36px;width:130px;height:62px;background:#fff;border:1px solid #d0d0d0}
.badge.dark{background:var(--navy-deep)}

/* contact */
.contact{left:0;top:2012px;width:1200px;height:372px;background:linear-gradient(120deg,#1a3068,#24417f 60%,#1a3068)}
.map{left:46px;top:28px;width:510px;height:322px;border:4px solid #e8e8e8;border-radius:8px;background:linear-gradient(180deg,#eef0ea,#e6e8e0 60%,#cfd9e8)}
.contact h2{position:absolute;left:672px;top:42px;font-size:24px;font-weight:400;color:#fff;width:458px;padding-bottom:18px;border-bottom:2px solid #fff}
.cline{position:absolute;left:676px;display:flex;gap:20px;color:#fff;font-size:16px;line-height:24px}
.cline svg{width:20px;height:20px;margin-top:2px;flex:none}

/* news */
.news{left:0;top:2384px;width:1200px;height:88px;background:#15285a}
.news .tag{position:absolute;left:68px;top:24px;display:flex;gap:10px;align-items:center;color:#fff}
.news .tag small{display:block;font-size:12px;line-height:14px}
.news .tag b{display:block;font-size:22px;font-weight:600;line-height:24px}
.ticker{position:absolute;left:270px;top:12px;width:780px;height:64px;background:#fff;display:flex;align-items:center;font-size:14px;color:#444;padding:0 24px}
.ticker .date{color:var(--navy);font-weight:600;margin:0 14px 0 26px;white-space:nowrap}
.ticker .msg{flex:1;white-space:nowrap;overflow:hidden;text-overflow:ellipsis}

/* footer lists */
.links{top:2472px;left:0;width:1200px;height:416px;background:#fff}
.links h4{position:absolute;top:62px;font-size:14px;font-weight:400;color:#333}
.links ul{position:absolute;top:102px;font-size:12.5px;color:#777;line-height:21px}
.links li::before{content:"»";margin-right:12px;color:#999}
.links li.wrap{padding-left:20px;text-indent:-20px}

.footnav{left:0;top:2888px;width:1200px;height:58px;background:var(--bar);display:flex;justify-content:center;align-items:center;gap:22px;color:#fff;font-size:13px;font-weight:600}
.copy{left:0;top:2946px;width:1200px;height:64px;background:var(--light);display:flex;align-items:center;justify-content:space-between;padding:0 70px;font-size:12px;color:#444}
.social{display:flex;gap:6px}
.social span{width:20px;height:20px;border-radius:50%;background:#2f5a9e}
.social span:last-child{background:#d2473a}
</style>
</head>
<body>

<svg width="0" height="0" style="position:absolute">
  <defs>
    <symbol id="ring" viewBox="0 0 56 56"><circle cx="28" cy="28" r="26" fill="none" stroke="#fff" stroke-width="2.5"/></symbol>
    <symbol id="g-car" viewBox="0 0 56 56"><use href="#ring"/><path d="M16 32h24v6H16zM19 32l3-8h12l3 8" fill="none" stroke="#fff" stroke-width="2.5"/><circle cx="21" cy="38" r="2" fill="#fff"/><circle cx="35" cy="38" r="2" fill="#fff"/></symbol>
    <symbol id="g-boat" viewBox="0 0 56 56"><use href="#ring"/><path d="M28 14v20l-10 0zM30 18l8 16h-8zM16 37h24l-4 5H20z" fill="#fff"/></symbol>
    <symbol id="g-chart" viewBox="0 0 56 56"><use href="#ring"/><rect x="17" y="32" width="5" height="8" fill="#fff"/><rect x="25" y="27" width="5" height="13" fill="#fff"/><rect x="33" y="22" width="5" height="18" fill="#fff"/><path d="M17 26l9-8 5 4 8-7" fill="none" stroke="#fff" stroke-width="2"/></symbol>
    <symbol id="g-house" viewBox="0 0 56 56"><use href="#ring"/><path d="M15 29l13-12 13 12h-4v11H19V29z" fill="#fff"/><rect x="25" y="32" width="6" height="8" fill="#1b2f66"/></symbol>
    <symbol id="g-bike" viewBox="0 0 56 56"><use href="#ring"/><circle cx="19" cy="35" r="5" fill="none" stroke="#fff" stroke-width="2.5"/><circle cx="37" cy="35" r="5" fill="none" stroke="#fff" stroke-width="2.5"/><path d="M19 35l8-9h7l3 9M27 26l-2-5" fill="none" stroke="#fff" stroke-width="2.5"/></symbol>
    <symbol id="g-building" viewBox="0 0 56 56"><use href="#ring"/><rect x="16" y="24" width="10" height="16" fill="#fff"/><rect x="28" y="16" width="12" height="24" fill="#fff"/></symbol>
    <symbol id="g-wave" viewBox="0 0 56 56"><use href="#ring"/><path d="M18 30l10-9 10 9v6H18z" fill="#fff"/><path d="M13 40q4-3 8 0t8 0 8 0 8 0" fill="none" stroke="#fff" stroke-width="2.5"/></symbol>
    <symbol id="g-plane" viewBox="0 0 56 56"><use href="#ring"/><path d="M16 32l24-12-6 16-6-5-4 6v-8z" fill="#fff"/><path d="M14 40h28" stroke="#fff" stroke-width="2"/></symbol>
    <symbol id="g-hand" viewBox="0 0 56 56"><use href="#ring"/><path d="M14 28l8-7 6 4 6-4 8 7-12 10z" fill="#fff"/></symbol>
    <symbol id="g-shield" viewBox="0 0 56 56"><use href="#ring"/><path d="M28 14l11 4v9c0 7-5 12-11 15-6-3-11-8-11-15v-9z" fill="#fff"/></symbol>
    <symbol id="g-leaf" viewBox="0 0 56 56"><use href="#ring"/><path d="M28 14c8 6 8 18 0 26-8-8-8-20 0-26zM28 22v20" fill="#fff" stroke="#2a2f3e" stroke-width="1.5"/></symbol>
    <symbol id="g-person" viewBox="0 0 56 56"><use href="#ring"/><circle cx="30" cy="17" r="3.5" fill="#fff"/><path d="M29 22l-6 9 6 2-3 9M29 22l8 6M25 28l-7-2" fill="none" stroke="#fff" stroke-width="3" stroke-linecap="round"/></symbol>
    <symbol id="g-gear" viewBox="0 0 56 56"><use href="#ring"/><circle cx="28" cy="28" r="8" fill="none" stroke="#fff" stroke-width="4"/><path d="M28 15v5M28 36v5M15 28h5M36 28h5" stroke="#fff" stroke-width="4"/></symbol>
    <symbol id="g-chair" viewBox="0 0 56 56"><use href="#ring"/><circle cx="27" cy="16" r="3" fill="#fff"/><path d="M27 21v10h9l3 8M23 26a9 9 0 1 0 10 12" fill="none" stroke="#fff" stroke-width="3"/></symbol>
    <symbol id="g-pin" viewBox="0 0 20 20"><path d="M3 9l7-6 7 6v8H3z" fill="none" stroke="#fff" stroke-width="2"/></symbol>
    <symbol id="g-phone" viewBox="0 0 20 20"><path d="M5 2l3 4-2 2c1 3 3 5 6 6l2-2 4 3-2 3C9 18 2 11 2 4z" fill="#fff"/></symbol>
  </defs>
</svg>

<nav class="topnav abs">
  <ul>
    <li class="active">HOME</li><li>ABOUT</li><li>FINANCIAL PLANINING</li><li>INVESTMENT MANAGEMENT</li><li>SERVICES</li><li>CONTACT</li>
  </ul>
  <span class="login">LOGIN</span>
</nav>

<header class="brandbar abs">
  <div class="brand"><span class="mark"></span>Crestmark Insurance Group</div>
</header>

<section class="hero abs" role="img" aria-label="Evening view over a historic city skyline with a tower and a domed cathedral under a dusk sky">
</section>
<div class="hero-text abs">
  <div class="l1">We have your</div>
  <div class="l2">Family and Business</div>
  <div class="l3">Covered</div>
</div>

<form class="quote abs">
  <h2>Get An Insurance Quote</h2>
  <div class="field" style="top:100px">NAME:</div>
  <div class="field" style="top:148px">PHONE:</div>
  <div class="field" style="top:196px">EMAIL:</div>
  <div class="typebox">
    CHOOSE INSURANCE TYPE :
    <div class="opts">
      <span><i class="on"></i>Personal</span><span><i></i>Business</span>
      <span><i></i>Life/Health</span><span><i></i>Benefits</span>
    </div>
  </div>
  <div class="quote-btn">GET A QUOTE <svg width="10" height="14" viewBox="0 0 10 14"><path d="M1 1l7 6-7 6z" fill="#fff"/></svg></div>
  <p class="quote-note">★ We won't use your email or phone number for any other purpose than contacting you.</p>
</form>

<section class="about abs">
  <div class="about-photo abs" role="img" aria-label="Faded group of business professionals standing together"></div>
  <h2>ABOUT US</h2>
  <div class="sub">CRESTMARK INSURANCE GROUP</div>
  <div class="rule"></div>
  <p>Established in 2015, Crestmark Insurance Group is a full service independent insurance agency. Our licensed agents have the experience to custom tailor a program to meet your specific needs &amp; our professional support staff will provide you with top notch customer service to help ease the burden of managing your insurance program.</p>
  <div class="btn-red">READ MORE</div>
</section>

<section class="panel personal abs">
  <h3>PERSONAL INSURANCE</h3>
  <ul class="items">
    <li class="item"><svg><use href="#g-car"/></svg>Auto Insurance</li>
    <li class="item"><svg><use href="#g-chart"/></svg>High Net Worth<br>Insurance</li>
    <li class="item"><svg><use href="#g-boat"/></svg>Boat &amp; Marine Insurance</li>
    <li class="item"><svg><use href="#g-house"/></svg>Rental and Investment<br>Property</li>
    <li class="item"><svg><use href="#g-car"/></svg>Collector Car Insurance</li>
    <li class="item"><svg><use href="#g-bike"/></svg>Motorcycle Insurance</li>
    <li class="item"><svg><use href="#g-building"/></svg>Condo Insurance</li>
    <li class="item"><svg><use href="#g-house"/></svg>Renters Insurance</li>
    <li class="item"><svg><use href="#g-wave"/></svg>Flood Insurance</li>
    <li class="item"><svg><use href="#g-plane"/></svg>Travel Insurance</li>
  </ul>
  <div class="btn-red">KNOW MORE</div>
</section>

<section class="panel business abs">
  <h3>BUSINESS INSURANCE</h3>
  <ul class="items">
    <li class="item"><svg><use href="#g-hand"/></svg>Bond Insurance</li>
    <li class="item"><svg><use href="#g-car"/></svg>Commercial Auto Insurance</li>
    <li class="item"><svg><use href="#g-shield"/></svg>Builders Risk Insurance</li>
    <li class="item"><svg><use href="#g-leaf"/></svg>Crop / Hail Insurance</li>
    <li class="item"><svg><use href="#g-person"/></svg>Cyber Insurance</li>
    <li class="item"><svg><use href="#g-shield"/></svg>Liability Insurance</li>
    <li class="item"><svg><use href="#g-person"/></svg>Crime Insurance</li>
    <li class="item"><svg><use href="#g-house"/></svg>Property Insurance</li>
    <li class="item"><svg><use href="#g-chair"/></svg>General Liability Insurance</li>
    <li class="item"><svg><use href="#g-gear"/></svg>Equipment Breakdown</li>
  </ul>
  <div class="btn-red">KNOW MORE</div>
</section>

<div class="tip abs">
  A Builders Risk Policy is a property insurance policy that is designed to cover property in the course of construction. There is no single standard builders risk form; most builders risk policies are written on inland marine (rather than commercial property) forms
  <span class="more">Read More ›</span>
</div>

<section class="partners abs" aria-label="Partner carriers">
  <div class="badge" style="left:74px"></div>
  <div class="badge" style="left:226px"></div>
  <div class="badge" style="left:376px"></div>
  <div class="badge dark" style="left:534px"></div>
  <div class="badge" style="left:684px"></div>
  <div class="badge" style="left:834px"></div>
  <div class="badge" style="left:984px"></div>
</section>

<section class="contact abs">
  <div class="map abs" role="img" aria-label="Street map showing the office location marked with an arrow"></div>
  <h2>CONTACTE US</h2>
  <div class="cline" style="top:140px"><svg><use href="#g-pin"/></svg><span>1820 Harbor Crest Avenue, Suite 300<br>Coral Bay, FL 33190</span></div>
  <div class="cline" style="top:210px"><svg><use href="#g-phone"/></svg><span>(555) 214-9188</span></div>
  <div class="cline" style="top:286px"><svg><use href="#g-phone"/></svg><span>(555) 307-1163</span></div>
</section>

<section class="news abs">
  <div class="tag">
    <svg width="44" height="40" viewBox="0 0 44 40"><rect x="2" y="2" width="34" height="34" fill="none" stroke="#fff" stroke-width="3"/><rect x="8" y="8" width="10" height="8" fill="#fff"/><path d="M22 10h9M22 15h9M8 22h23M8 28h23M36 12h5v22a4 4 0 0 1-5 2" fill="none" stroke="#fff" stroke-width="2.5"/></svg>
    <div><small>IN THE</small><b>NEWS</b></div>
  </div>
  <div class="ticker">
    <svg width="10" height="18" viewBox="0 0 10 18"><path d="M9 1L1 9l8 8" fill="none" stroke="#333" stroke-width="2"/></svg>
    <span class="date">April 21, 2016:</span>
    <span class="msg">Lorem ipsum dolor sit amet, consectetuer adipiscing elit. Aenean commodo ligula eget dolor.</span>
    <svg width="10" height="18" viewBox="0 0 10 18" style="margin-left:24px;flex:none"><path d="M1 1l8 8-8 8" fill="none" stroke="#333" stroke-width="2"/></svg>
  </div>
</section>

<section class="links abs">
  <h4 style="left:70px">BUSINESS INSURANCE</h4>
  <ul style="left:70px">
    <li>Bond Insurance</li><li>Builders Risk Insurance</li><li>Business Owners Policy (BOP)</li><li>Commercial Auto Insurance</li><li>Crime Insurance</li><li>Crop / Hail Insurance</li><li>Difference in Conditions</li><li>Directors and Officers (D&amp;O)</li><li>Employment Practices Liability</li><li>Errors &amp; Omissions (E&amp;O)</li><li>Equipment Breakdown</li><li>Garage Insurance</li>
  </ul>
  <ul style="left:362px;width:240px">
    <li>General Liability Insurance</li><li>Inland Marine Insurance</li><li>Liquor Liability Insurance</li><li>Medical Malpractice Insurance</li><li class="wrap">Owners and Contractors Protective Liability (OCP)</li><li>Professional Liability</li><li>Property Insurance</li><li>Truckers Insurance</li><li>Umbrella Insurance</li><li class="wrap">Workers Compensation / Employer Liability</li>
  </ul>
  <h4 style="left:654px">PERSONAL INSURANCE</h4>
  <ul style="left:654px">
    <li>Auto Insurance</li><li>Boat &amp; Marine Insurance</li><li>Collector Car Insurance</li><li>Condo Insurance</li><li>Flood Insurance</li><li>High Net Worth Insurance</li><li>Homeowners Insurance</li><li>Rental and Investment Property</li><li>Mobile Home Insurance</li><li>Motor Home Insurance</li><li>Motorcycle Insurance</li><li>Personal Umbrella Insurance</li>
  </ul>
  <ul style="left:940px">
    <li>Recreational Vehicles</li><li>Renters Insurance</li><li>Travel Insurance</li><li>Valuable Items Insurance</li>
  </ul>
</section>

<nav class="footnav abs">
  <span>Home</span><span>About</span><span>Financial Planning</span><span>Investment Management</span><span>Services</span><span>Contact</span>
</nav>

<footer class="copy abs">
  <span>Copyright © 2016 Crestmark Insurance Group. All rights reserved.</span>
  <div class="social"><span></span><span></span><span></span><span></span></div>
</footer>

</body>
</html>
```